Cool Landing page with email address sign up (mockups provided)

I need a landing page for a service that will send a weekly email to people who are looking for jobs in startups. On the landing page there is a call to action (submit button) to register their email address. The service is called VentureRoster and it is a side project to try to assist startup companies with hiring people.

I just want one single form field "Email".

The feeling I want to give people is one of adventure. Imagine the person is living in Gdansk Poland, they are a technical/IT expert and have dreams of making it big in a Startup in London. This is his big chance, this is going to allow him to do it! He's signing up to a big promise! It should be cool, professional, exciting.

A major influence should be:
http://copperkettlefair.example/

There should also be a call to tweet in a cool way like on (http://www.behindfounders.example/).

Look at this - taking a leap of faith, like this:
http://pagebloomkit.example/wp-content/uploads/2011/09/19.jpg

This is super with the colours - striking!:
http://hueparlor.example/

Fly your kit higher!:
http://tobiasvrenn.example/

If necessary use sex to sell:
http://pagebloomkit.example/wp-content/uploads/2011/09/24.jpg

Some original art would work:
http://pagebloomkit.example/wp-content/uploads/2011/09/fx_ss_group1_sm_filtered_0000s_0007_Layer-14.jpg

This is effective for a call to action, I'm looking to you to act!:
http://pagebloomkit.example/wp-content/uploads/2011/09/weblance.jpg
Take inspiration from:
http://www.behindfounders.example/
http://ventureroster.example/
http://foundersdaily.example/

***N.B.: I would prefer original art background over a photo

Also:
http://pixeljournalhub.example/inspiration/a-showcase-of-landing-pages-designed-for-conversion
especially:
http://pixeljournalhub.example/wp-content/uploads/2011/09/01-landing.jpg
http://pixeljournalhub.example/wp-content/uploads/2011/09/04-landing.jpg
http://pixeljournalhub.example/wp-content/uploads/2011/10/texture21.jpg

I really like the colouring from Coder Bulletin:
http://news.quillforge.example/

Reason: I'm going to be away for a few days so I won't have enough time to properly provide feedback.

The payment is now guaranteed. This project is a single page only.

I've added a few more example landing pages that I like.

I've now added the ventureroster logo image that should be used.

I've updated brief with more examples of what I'm looking for

Reason: I'm still progressing with candidate designs.

Target Market(s)

Technical people, english not being their native language. Ambitious to work in London/Dublin in a tech startup company. They want to receive a weekly emails with startup jobs in london or dublin.

Requirements
Must have
• Eyes must be drawn to the email registration form to get them to submit their email address. The background image or website theme should encourage their desires to work in the big city in exciting startup companies.

Should have a prompt to tweet (once pressed I'll do my own popup)

```html
<!DOCTYPE html>
<html lang="en">
<head>
<meta charset="utf-8">
<title>VentureRoster – Startup jobs in London and Dublin</title>
<link rel="stylesheet" href="https://fonts.googleapis.com/css2?family=Bodoni+Moda:ital,wght@0,500;1,500&family=Jost:wght@500;600&family=Open+Sans:wght@400&family=Varela+Round&display=swap">
<style>
  :root {
    --sky: #cfe5ea;
    --ground: #a39d7c;
    --ground-light: #c7c0a0;
    --panel: #aea78a;
    --footer: #7b7459;
    --text-light: #ffffff;
    --text-dark: #6f6a52;
    --accent: #f2c46a;
    --logo-grey: #7a7a72;
    --logo-green: #8cc63f;
    --field: #b8b294;
    --divider: #8a8468;
  }
  * { box-sizing: border-box; margin: 0; padding: 0; }
  html, body { width: 1123px; height: 1200px; overflow: hidden; }
  body {
    position: relative;
    background: var(--ground);
    font-family: "Open Sans", sans-serif;
    color: var(--text-light);
  }
  .sky {
    position: absolute; left: 0; top: 0; width: 1123px; height: 488px;
    background: var(--sky);
  }
  .ground {
    position: absolute; left: 0; top: 488px; width: 1123px; height: 624px;
    background: radial-gradient(ellipse 420px 170px at 560px 20px, var(--ground-light), var(--ground) 80%);
  }
  .logo {
    position: absolute; left: 72px; top: 20px;
    display: flex; align-items: center; gap: 8px;
    font-family: "Jost", sans-serif; font-weight: 500; font-size: 40px;
    color: var(--logo-grey); letter-spacing: -0.5px;
  }
  .logo .dot {
    width: 14px; height: 14px; border-radius: 50%; background: var(--logo-green);
  }
  .main-nav {
    position: absolute; right: 84px; top: 18px;
    display: flex; gap: 24px;
    font-family: "Bodoni Moda", serif; font-size: 25px; font-weight: 500;
  }
  .main-nav a { color: var(--text-dark); text-decoration: none; padding-bottom: 4px; }
  .main-nav a.current { font-style: italic; border-bottom: 2px solid var(--text-dark); }
  .skyline {
    position: absolute; left: 154px; top: 72px; width: 804px; height: 416px;
    background: linear-gradient(180deg, var(--sky) 0%, #e2d7a4 40%, #b9a788 75%, #8f8163 100%);
    border-radius: 40px 40px 0 0;
    opacity: 0.85;
  }
  .headline {
    position: absolute; left: 74px; top: 526px; width: 500px;
    font-family: "Jost", sans-serif; font-weight: 600; font-size: 31px;
    line-height: 33px; letter-spacing: -0.6px;
    text-shadow: 0 1px 1px rgba(0,0,0,0.15);
  }
  .headline .soft { color: #efe9d4; }
  .headline .accent { color: var(--accent); }
  .signup {
    position: absolute; left: 92px; top: 689px; width: 187px;
  }
  .signup input, .signup button {
    display: block; width: 187px; height: 26px;
    border: 1px solid #c9c3a6; background: var(--field);
    font-family: "Open Sans", sans-serif; font-size: 11px; color: #ebe6d2;
  }
  .signup input { padding-left: 8px; }
  .signup input::placeholder { color: #ebe6d2; }
  .signup button {
    margin-top: 7px; font-family: "Jost", sans-serif; font-weight: 600;
    font-size: 13px; color: #fff; background: linear-gradient(#c3bd9f, #aca68a);
  }
  .signup-note {
    position: absolute; left: 325px; top: 686px; width: 250px;
    font-family: "Jost", sans-serif; font-weight: 600; font-size: 19px; line-height: 24px;
    letter-spacing: -0.3px;
  }
  .info-box {
    position: absolute; left: 72px; width: 489px; height: 124px;
    background: var(--panel); border-radius: 5px; padding: 10px 16px;
  }
  .info-box.how { top: 782px; }
  .info-box.companies { top: 940px; }
  .info-box h2 {
    font-family: "Bodoni Moda", serif; font-weight: 500; font-size: 24px; line-height: 28px;
  }
  .info-box.how h2 { font-style: italic; }
  .info-box p { font-size: 10.5px; line-height: 13.5px; margin-top: 4px; }
  .divider {
    position: absolute; left: 649px; top: 660px; width: 2px; height: 344px;
    background: var(--divider);
  }
  .share-title {
    position: absolute; left: 773px; top: 532px;
    font-family: "Bodoni Moda", serif; font-style: italic; font-size: 23px; color: #f2efe2;
  }
  .share-icons { position: absolute; left: 773px; top: 568px; display: flex; gap: 9px; }
  .share-icons .icon {
    width: 38px; height: 38px; background: #d6d0b6; border-radius: 3px;
    display: flex; align-items: center; justify-content: center;
  }
  .share-icons .icon.tweet { border-radius: 50%; width: 62px; background: transparent; }
  .share-icons .icon.tweet span { width: 38px; height: 38px; border-radius: 50%; background: #d6d0b6; }
  .news-title {
    position: absolute; left: 771px; top: 636px;
    font-family: "Bodoni Moda", serif; font-size: 23px; color: #f2efe2;
  }
  .news-box {
    position: absolute; left: 739px; top: 675px; width: 299px; height: 304px;
    background: var(--panel); border-radius: 5px; padding: 18px 30px 0 32px;
  }
  .news-item h3 {
    font-family: "Varela Round", sans-serif; font-weight: 400; font-size: 20px; line-height: 24px;
  }
  .news-item p { font-size: 10.5px; line-height: 13.2px; margin-top: 2px; }
  .news-item + .news-item { margin-top: 14px; }
  .more {
    display: inline-block; width: 10px; height: 10px; background: #d6d0b6;
    vertical-align: middle; margin-left: 3px; position: relative;
  }
  .archive {
    position: absolute; right: 14px; bottom: 8px;
    font-family: "Open Sans", sans-serif; font-style: italic; font-size: 12.5px;
  }
  .site-footer {
    position: absolute; left: 0; top: 1112px; width: 1123px; height: 88px;
    background: var(--footer); font-size: 11px; letter-spacing: 0.5px;
  }
  .site-footer .copyright { position: absolute; left: 74px; top: 19px; }
  .site-footer nav { position: absolute; left: 382px; top: 19px; display: flex; gap: 14px; }
  .site-footer nav a { color: var(--accent); text-decoration: none; }
</style>
</head>
<body>
  <div class="sky"></div>
  <div class="ground"></div>

  <header>
    <div class="logo"><span>ventureroster</span><span class="dot"></span></div>
    <nav class="main-nav">
      <a class="current" href="#how">How it works</a>
      <a href="#companies">Companies</a>
      <a href="#news">News</a>
    </nav>
  </header>

  <div class="skyline" role="img" aria-label="Illustrated skyline of London and Dublin landmarks: a red double-decker bus with a Union flag, Tower Bridge, Big Ben, the London Eye, a red phone box and a Dublin church with the Irish flag"></div>

  <h1 class="headline">Are you a technical person <span class="soft">ambitious</span> to work in London or Dublin? If you are, then you should definitely hit the <span class="accent">subscribe</span> button bellow.</h1>

  <form class="signup" action="#">
    <input type="email" name="email" placeholder="Your e-mail here" aria-label="Email">
    <button type="submit">SUBSCRIBE</button>
  </form>
  <p class="signup-note">Receive weekly emails with startup jobs in London and Dublin.</p>

  <section class="info-box how" id="how">
    <h2>How it works</h2>
    <p>Donec mollis mollis neque, ut suscipit dui pellentesque ullamcorper. Sedir vel risus diam, eget lobortis risus. Suspe ndisse sed risus hen drerit qura am vulputate tinci dunt sit amet sed purus. Praesent sed est quis maurg is rutrum elementum. Nunc vitae pretium sem. Nullam dapibus placeratia tincidunt.</p>
  </section>

  <section class="info-box companies" id="companies">
    <h2>Companies</h2>
    <p>Quisque at melus arcu non scelerisque lacus. Duis pharetra mi arcu. Sedir viverra quis hendrerit urna blandit. Mauris tincidunt tristique elit, ultricesca velit malesuada eget. Aliquam aliquet cursus ipsum, eu fringilla augueriu molestie eget. Etiam blandit tempor justo, sed scelerisque ante ultriciesec elementum.</p>
  </section>

  <div class="divider"></div>

  <aside>
    <h2 class="share-title">Share this</h2>
    <div class="share-icons">
      <a class="icon tweet" href="#" aria-label="Tweet"><span></span></a>
      <a class="icon" href="#" aria-label="Share by email">
        <svg width="26" height="18" viewBox="0 0 26 18"><rect x="1" y="1" width="24" height="16" fill="#fff" stroke="#b8b294"/><path d="M1 1 L13 10 L25 1" fill="none" stroke="#b8b294" stroke-width="1.5"/></svg>
      </a>
      <a class="icon" href="#" aria-label="Feed">
        <svg width="22" height="22" viewBox="0 0 22 22"><circle cx="4" cy="18" r="3" fill="#fff"/><path d="M2 9a11 11 0 0 1 11 11" fill="none" stroke="#fff" stroke-width="3"/><path d="M2 2a18 18 0 0 1 18 18" fill="none" stroke="#fff" stroke-width="3"/></svg>
      </a>
    </div>

    <h2 class="news-title" id="news">Lates news</h2>
    <div class="news-box">
      <article class="news-item">
        <h3>Lorem ipsum</h3>
        <p>Nam lobortis, sem eget venenatis blandit, quam odio posuere nibh, vel porttitor lacus lorem a leo. Cras sit amet mollis risus. Vivamus ac purus eu libero sollicitudin pretium. Maecenas eget dui quis neque posuere venenatis. Aenean adipiscing molestie magna, eget lobortis turpis volutpat a.<span class="more"></span></p>
      </article>
      <article class="news-item">
        <h3>Dolor sit amet</h3>
        <p>Vivamus ac purus eu libero sollicitudin pretium. Maecenas eget dui quis neque posuere venenatis. Aenean adipiscing molestie magna, eget lobortis turpis volutpat a.<span class="more"></span></p>
      </article>
      <a class="archive" href="#" style="color:#fff;text-decoration:none">Archive</a>
    </div>
  </aside>

  <footer class="site-footer">
    <p class="copyright">©2011 VentureRoster - All Rights Reserved</p>
    <nav>
      <a href="#">Terms</a>
      <a href="#">Privacy</a>
      <a href="#">Contact</a>
    </nav>
  </footer>
</body>
</html>
```